Reiki business card

Please see uploaded files. There is a word document on there explaining what is required and what the other uploaded files are for. I am after a soft, relaxing, warm welcoming feel to the card. Thank you.

Business

```html
<!DOCTYPE html>
<html lang="en">
<head>
<meta charset="utf-8">
<title>Willowbrook Energy Care – Business Card</title>
<link rel="stylesheet" href="https://fonts.googleapis.com/css2?family=Arimo:wght@700&family=Roboto+Condensed:wght@700&display=swap">
<style>
  :root {
    --stage: #3a3a3a;
    --sky: #00aeef;
    --sky-mid: #1fb6f0;
    --sky-pale: #79d3f7;
    --sky-mist: rgba(180, 232, 252, 0.45);
    --white: #ffffff;
  }
  * { margin: 0; padding: 0; box-sizing: border-box; }
  html, body {
    width: 1200px; height: 1200px; overflow: hidden;
    background: var(--stage);
  }
  .card {
    position: absolute; left: 248px;
    width: 687px; height: 420px;
    background: var(--sky); overflow: hidden;
  }
  .card--front { top: 130px; }
  .card--back { top: 614px; height: 419px; }
  .rays { position: absolute; inset: 0; width: 100%; height: 100%; }
  .artwork {
    position: absolute; left: 0; top: 0; width: 250px; height: 100%;
    background: linear-gradient(160deg, rgba(255,255,255,0.8), rgba(255,255,255,0.35) 70%, rgba(255,255,255,0.15));
  }
  .title-panel {
    position: absolute; left: 277px; top: 95px; width: 410px; height: 124px;
    background: var(--sky-mist);
    display: flex; align-items: center; justify-content: center; text-align: center;
  }
  .title {
    font-family: "Arimo", Arial, sans-serif;
    font-weight: 700;
    color: var(--white); font-size: 38px; line-height: 50px;
  }
  .contact-box {
    position: absolute; left: 409px; top: 347px; width: 278px; height: 73px;
    background: var(--white);
    font-family: "Arimo", Arial, sans-serif; font-weight: 700;
    color: var(--sky); text-align: center; font-size: 25px; line-height: 33px;
    padding-top: 5px;
  }
  .tagline-band {
    position: absolute; left: 0; top: 129px; width: 100%; height: 119px;
    background: var(--white);
    display: flex; align-items: center; justify-content: center; text-align: center;
    font-family: "Roboto Condensed", "Arial Narrow", sans-serif; font-weight: 700;
    color: var(--sky); font-size: 40px; line-height: 53px;
  }
  .email-band {
    position: absolute; left: 0; top: 274px; width: 100%; height: 63px;
    background: var(--white);
    display: flex; align-items: center; justify-content: center;
    font-family: "Arimo", Arial, sans-serif; font-weight: 700;
    color: var(--sky); font-size: 27px;
  }
</style>
</head>
<body>
  <section class="card card--front">
    <svg class="rays" viewBox="0 0 687 420" aria-hidden="true">
      <polygon points="277,95 687,0 687,345 532,345 277,219" fill="var(--sky-mid)"/>
      <polygon points="277,95 687,20 687,292 277,219" fill="var(--sky-pale)"/>
    </svg>
    <div class="artwork" role="img" aria-label="White silhouette of a blossoming tree with a child hugging a dog beneath it"></div>
    <div class="title-panel">
      <h1 class="title">Willowbrook<br>Energy Care</h1>
    </div>
    <div class="contact-box">
      <p class="contact-name">Maren Holloway</p>
      <p class="contact-phone">0400 123 987</p>
    </div>
  </section>

  <section class="card card--back">
    <svg class="rays" viewBox="0 0 687 419" aria-hidden="true">
      <polygon points="0,129 687,0 687,56" fill="var(--sky-mid)"/>
      <polygon points="0,129 687,56 687,129" fill="var(--sky-pale)"/>
      <rect x="0" y="248" width="687" height="26" fill="var(--sky-mid)"/>
      <polygon points="240,274 687,248 687,274" fill="var(--sky-pale)"/>
      <polygon points="0,337 687,337 0,385" fill="var(--sky-pale)"/>
      <polygon points="0,385 687,337 0,419" fill="var(--sky-mid)"/>
    </svg>
    <p class="tagline-band">REIKI - RELAXES, RESTORES BALANCE<br>&amp; PROMOTES HEALING</p>
    <p class="email-band">willowbrookenergycare@mailbox.com</p>
  </section>
</body>
</html>
```